Email Design Creative Design Needed

Our website is called CampusLedger.org. One of our competitor(varsity scout.us.com) is using the following email creative.
http://qtr.brightvelmo.com/Affiliate/Assets/3532.html
http://qtr.brightvelmo.com/Affiliate/Assets/7921.html
http://qtr.brightvelmo.com/Affiliate/Assets/8061.html

We would like to use similar email creative without copying their exact creative. You can use the above as a guide but then come up with your own version of the creative.
The above are just concepts, please be creative and come up with your own version of it, without feeling that they have been copied. Feel free to move the components around. Also, feel free to change the colours and text.

Please find attached the CampusLedger.org logo.

Reason: We would like to receive more designs.

Industry/Entity Type

College

```html
<!DOCTYPE html>
<html lang="en">
<head>
<meta charset="utf-8">
<title>CampusLedger.org – Earn an Accredited Degree</title>
<link href="https://fonts.googleapis.com/css2?family=Barlow:wght@500;600;700&family=Roboto:wght@400;500;700&display=swap" rel="stylesheet">
<style>
  :root {
    --page: #ffffff;
    --navy: #14284b;
    --navy-deep: #0d1b35;
    --teal: #0f7c8a;
    --teal-light: #3fb3bf;
    --gold: #f2b632;
    --cream-a: #f6f1e7;
    --cream-b: #e6ddcc;
    --cell-bg: #ffffff;
    --ink: #22303f;
    --muted: #5a6675;
    --link: #0f7c8a;
  }
  * { box-sizing: border-box; margin: 0; padding: 0; }
  html, body { width: 1200px; height: 1200px; overflow: hidden; background: var(--page); }
  .canvas { position: relative; width: 1200px; height: 1200px; font-family: "Roboto", Arial, sans-serif; color: var(--ink); }

  /* Masthead */
  .masthead { position: absolute; left: 84px; top: 0; width: 1035px; height: 100px; background: var(--navy); }
  .brand { position: absolute; left: 32px; top: 26px; display: flex; align-items: center; gap: 14px; }
  .brand-dot { width: 36px; height: 36px; border-radius: 50%; background: var(--gold); }
  .brand-name { font-family: "Barlow", Arial, sans-serif; font-weight: 600; font-size: 46px; line-height: 1; color: #ffffff; }

  /* Hero */
  .hero { position: absolute; left: 84px; top: 100px; width: 1035px; height: 340px; overflow: hidden;
    background: linear-gradient(120deg, var(--cream-a) 0%, var(--cream-b) 100%); }
  .promo { position: absolute; left: 40px; top: 62px; width: 560px; height: 230px; background: var(--gold); }
  .promo-inner { position: absolute; left: 0; top: 0; width: 548px; height: 218px; background: var(--teal);
    padding: 30px 0 0 36px; }
  .promo-title { font-family: "Barlow", Arial, sans-serif; font-weight: 600; font-size: 40px; line-height: 50px; color: #ffffff; }
  .promo-title .highlight { color: var(--gold); }
  .student-photo { position: absolute; left: 660px; top: 24px; width: 300px; height: 316px; border-radius: 150px 150px 0 0;
    background: linear-gradient(180deg, #8a94a3 0%, #56627a 55%, #dfe2e6 100%); }
  .cap-art { position: absolute; left: 905px; top: 18px; width: 110px; height: 74px; border-radius: 12px;
    background: linear-gradient(160deg, #3b4656 0%, var(--navy-deep) 100%); }

  .accent-line { position: absolute; left: 84px; top: 440px; width: 1035px; height: 6px; background: var(--gold); }

  /* Salary board */
  .salary-board { position: absolute; left: 84px; top: 446px; width: 1035px; height: 474px;
    background: linear-gradient(160deg, var(--navy) 0%, #17406a 55%, var(--teal) 100%); }
  .board-head { position: absolute; left: 0; top: 0; width: 100%; height: 80px; background: rgba(255,255,255,0.08);
    border-bottom: 2px solid rgba(242,182,50,0.6); }
  .head-label { position: absolute; top: 22px; font-family: "Barlow", Arial, sans-serif; font-weight: 600; font-size: 30px; line-height: 36px; color: #ffffff; }
  .head-label.col-occupation { left: 40px; }
  .head-label.col-salary { left: 378px; }
  .head-label.col-next { left: 700px; }

  .row { position: absolute; left: 28px; width: 979px; height: 80px; display: flex; gap: 10px; }
  .cell { background: var(--cell-bg); height: 100%; border-radius: 4px; display: flex; flex-direction: column; justify-content: center;
    font-size: 16px; line-height: 21px; }
  .cell.occupation { width: 320px; padding: 0 16px; border-left: 5px solid var(--gold); }
  .cell.salary { width: 310px; align-items: center; }
  .cell.next-step { width: 339px; padding: 0 20px; color: var(--link); font-weight: 500; }
  .get-started { color: var(--teal); font-weight: 700; font-size: 14px; margin-top: 3px; }
  .salary-amount { font-family: "Barlow", Arial, sans-serif; font-weight: 700; font-size: 26px; line-height: 30px; color: var(--navy); }
  .salary-unit { font-size: 14px; line-height: 18px; color: var(--muted); }

  /* Mission band */
  .mission { position: absolute; left: 84px; top: 920px; width: 1035px; height: 98px; background: var(--navy-deep);
    padding: 12px 56px 0; text-align: center; color: #ffffff; font-weight: 500; font-size: 15px; line-height: 19px; }
  .mission strong { color: var(--gold); font-weight: 700; }

  /* Fine print */
  .fine-print { position: absolute; left: 84px; top: 1048px; width: 1035px; text-align: center; font-size: 14px; line-height: 19px; color: var(--muted); }
  .fine-print .outcomes { margin-top: 16px; }
</style>
</head>
<body>
<div class="canvas">
  <header class="masthead">
    <div class="brand">
      <span class="brand-dot"></span>
      <span class="brand-name">CampusLedger.org</span>
    </div>
  </header>

  <section class="hero">
    <div class="promo">
      <div class="promo-inner">
        <h1 class="promo-title">Earn Your Degree From<br><span class="highlight">Accredited Colleges</span><br>&amp; Universities</h1>
      </div>
    </div>
    <div class="student-photo" role="img" aria-label="Photo of a smiling student carrying a shoulder bag"></div>
    <div class="cap-art" role="img" aria-label="Graduation cap illustration"></div>
  </section>

  <div class="accent-line"></div>

  <section class="salary-board">
    <div class="board-head">
      <span class="head-label col-occupation">Career Path</span>
      <span class="head-label col-salary">Median Pay</span>
      <span class="head-label col-next">Explore Programs</span>
    </div>

    <div class="row" style="top:106px">
      <div class="cell occupation"><span>Elementary and Secondary School Teachers</span><span class="get-started">Get Started &rarr;</span></div>
      <div class="cell salary"><span class="salary-amount">$51,290</span><span class="salary-unit">per year*</span></div>
      <div class="cell next-step">Elementary and Secondary<br>School Programs</div>
    </div>

    <div class="row" style="top:196px">
      <div class="cell occupation"><span>Educational, Guidance, School and<br>Vocational Counselors</span><span class="get-started">Get Started &rarr;</span></div>
      <div class="cell salary"><span class="salary-amount">$90,200</span><span class="salary-unit">per year*</span></div>
      <div class="cell next-step">Educational, Guidance, School and<br>Vocational Counselor Programs</div>
    </div>

    <div class="row" style="top:286px">
      <div class="cell occupation"><span>Elementary School Teachers,<br>Except Special Education</span><span class="get-started">Get Started &rarr;</span></div>
      <div class="cell salary"><span class="salary-amount">$90,200</span><span class="salary-unit">per year*</span></div>
      <div class="cell next-step">Elementary School Teacher Programs,<br>Except Special Education</div>
    </div>

    <div class="row" style="top:376px">
      <div class="cell occupation"><span>Preschool and Childcare Centers</span><span class="get-started">Get Started &rarr;</span></div>
      <div class="cell salary"><span class="salary-amount">$56,540</span><span class="salary-unit">per year*</span></div>
      <div class="cell next-step">Early Childhood Education<br>Programs</div>
    </div>
  </section>

  <section class="mission">
    At <strong>campusledger.org</strong>, we help you line up your education with your personal goals. Search for an accredited online degree by subject, level, school or program and let CampusLedger do the matching. Hundreds of programs from accredited online colleges and campus-based schools are listed, and many are built for working professionals who want to keep their current career while they study.
  </section>

  <footer class="fine-print">
    <p>*Median salaries according to the U.S. Bureau of Labor Statistics</p>
    <p>Disclaimer: Financial aid is available for those who qualify. To see if you qualify for financial aid of any kind you must speak<br>with a representative of one of our partnering schools.</p>
    <p class="outcomes">Program outcomes vary according to each institution's specific curriculum, and employment opportunities are not guaranteed.</p>
  </footer>
</div>
</body>
</html>
```